Advertisement Coaching practice

I need an advertisement (to be printed in newspaper). I have a coaching practice where I offer coaching, workshops family constellations and relationship therapy. The ad needs to express calmness, inspiration to transform but also not dull and boring. It would be great if you could use the colors from my logo into the ad.

Dimensions are: 13,04 cm Width x 9,72 cm Height.

I will add my previous self-made ad, my company logo, a portrait photo of myself and the text I want to add. Also my contact details should be visible as well.

Requirements
Nice to have
• I have updated the brief with a flyer that I had previously made by a designer. It would be a nice to have if the ad ties in with that. You can also look at my website at www.bravemoor.nu to see what colors I used there.

```html
<!DOCTYPE html>
<html lang="nl">
<head>
<meta charset="utf-8">
<title>Bravemoor – advertentie</title>
<link rel="stylesheet" href="https://fonts.googleapis.com/css2?family=Bebas+Neue&family=Montserrat:wght@400;500;700&family=PT+Sans&display=swap">
<style>
  :root {
    --gold: #a5863a;
    --gold-light: #bfa765;
    --gold-deep: #9b7c2f;
    --navy: #0b4a6e;
    --ink: #1a1a1a;
    --white: #ffffff;
    --grey: #555555;
  }
  html, body { margin: 0; padding: 0; width: 1200px; height: 1200px; overflow: hidden; background: var(--white); }
  .canvas { position: relative; width: 1200px; height: 1200px; }
  .ad {
    position: absolute; left: 233px; top: 336px;
    width: 1202px; height: 870px;
    transform: scale(.625); transform-origin: 0 0;
    overflow: hidden; outline: 1px solid #666;
    font-family: "Montserrat", sans-serif; color: var(--ink);
  }
  .ad-shapes { position: absolute; inset: 0; }
  .brand { position: absolute; left: 0; width: 745px; top: 38px; text-align: center; }
  .brand-mark { width: 64px; height: 64px; border: 3px solid #8a8a8a; border-radius: 50%; margin: 0 auto 14px; box-sizing: border-box; }
  .brand-name { font-family: "PT Sans", sans-serif; font-size: 44px; color: #4d4d4d; line-height: 1; letter-spacing: 1px; }
  .headline {
    position: absolute; left: 40px; width: 700px; top: 212px; margin: 0; text-align: center;
    font-family: "Bebas Neue", sans-serif; font-weight: 400; font-size: 56px; line-height: 50px; color: var(--navy);
  }
  .intro {
    position: absolute; left: 60px; width: 590px; top: 332px; margin: 0; text-align: center;
    font-size: 17.5px; line-height: 23px; font-weight: 500; text-transform: uppercase;
  }
  .benefits { position: absolute; left: 74px; top: 416px; margin: 0; padding: 0; list-style: none; font-size: 20px; line-height: 26px; font-weight: 500; }
  .benefits li { position: relative; padding-left: 28px; max-width: 480px; }
  .benefits li::before {
    content: ""; position: absolute; left: 2px; top: 5px; width: 13px; height: 13px;
    border: 2px solid var(--navy); border-radius: 50%;
  }
  .info-box {
    position: absolute; left: 80px; top: 598px; width: 1025px; height: 129px; box-sizing: border-box;
    border: 2px solid var(--navy); border-radius: 12px; padding: 10px 18px 0 22px;
    color: var(--white); font-size: 20px; line-height: 27px; text-align: justify;
  }
  .info-box p { margin: 0; }
  .website {
    position: absolute; left: 0; width: 1202px; top: 738px; text-align: center;
    color: var(--white); font-size: 26px; letter-spacing: 3px; line-height: 32px;
  }
  .website svg { vertical-align: -3px; margin-right: 8px; }
  .website strong { font-weight: 700; }
  .contact-bar {
    position: absolute; left: 0; top: 777px; width: 1202px; height: 93px; background: var(--navy);
    color: var(--white); display: flex; align-items: center;
  }
  .contact-name { position: absolute; left: 74px; font-size: 27px; font-weight: 700; letter-spacing: .5px; }
  .contact-name span { color: var(--gold-light); }
  .divider { position: absolute; top: 18px; width: 2px; height: 50px; background: var(--gold); }
  .contact-mail { position: absolute; left: 457px; font-size: 27px; font-weight: 500; display: flex; align-items: center; gap: 12px; }
  .contact-phone { position: absolute; left: 855px; display: flex; align-items: center; gap: 18px; font-family: "Bebas Neue", sans-serif; font-size: 48px; line-height: 1; padding-top: 4px; }
</style>
</head>
<body>
<div class="canvas">
  <div class="ad">
    <svg class="ad-shapes" width="1202" height="870" viewBox="0 0 1202 870">
      <defs>
        <linearGradient id="swoosh" x1="0" y1="1" x2="1" y2="0">
          <stop offset="0" stop-color="#9b7c2f"/>
          <stop offset="1" stop-color="#c2ab6b"/>
        </linearGradient>
        <linearGradient id="portrait-tones" x1="0" y1="0" x2="1" y2="1">
          <stop offset="0" stop-color="#4b4540"/>
          <stop offset=".45" stop-color="#8a6a52"/>
          <stop offset="1" stop-color="#9fb0c8"/>
        </linearGradient>
      </defs>
      <rect width="1202" height="870" fill="var(--white)"/>
      <path d="M0,220 C110,105 250,18 410,6 C260,30 120,115 0,190 Z" fill="url(#swoosh)"/>
      <path d="M0,527 C240,650 560,580 735,330 L1202,330 L1202,870 L0,870 Z" fill="var(--gold)"/>
      <path d="M245,585 C470,592 650,480 735,330 L760,345 C650,500 470,596 245,585 Z" fill="var(--white)"/>
      <path d="M245,585 C470,594 640,470 712,312 L740,328 C650,500 480,600 245,585 Z" fill="var(--gold-light)"/>
      <circle cx="1062" cy="215" r="372" fill="var(--gold-light)"/>
      <g role="img" aria-label="Portretfoto van de coach, glimlachend, in een lichtblauwe blouse">
        <circle cx="1062" cy="215" r="344" fill="url(#portrait-tones)"/>
      </g>
    </svg>

    <div class="brand">
      <div class="brand-mark"></div>
      <div class="brand-name">bravemoor</div>
    </div>

    <h1 class="headline">Coaching&nbsp; - Familieopstellingen<br>&amp; Relatietherapie</h1>

    <p class="intro">Trauma’s en negatieve ervaringen vormen ons en blijven nog lang voelbaar. Ze kunnen groei of geluk in de weg staan.</p>

    <ul class="benefits">
      <li>Doorbreken van belemmerende patronen;</li>
      <li>Beter omgaan met conflicten;</li>
      <li>In gezonde verbinding met elkaar als koppel of met anderen komen;</li>
    </ul>

    <div class="info-box">
      <p>Maandelijks geef ik workshops familieopstellingen.</p>
      <p>Ook houd ik themasessies rond adoptie, moeder-dochterdynamiek of relaties. Ook bied ik individuele coaching, relatietherapie en retraites aan. Kijk op de website voor meer info of neem contact op en ontdek wat het beste bij jou past.</p>
    </div>

    <div class="website">
      <svg width="24" height="24" viewBox="0 0 24 24" fill="none" stroke="currentColor" stroke-width="1.8"><circle cx="12" cy="12" r="10"/><ellipse cx="12" cy="12" rx="4.5" ry="10"/><path d="M2 12h20M4 7h16M4 17h16"/></svg>WWW.<strong>BRAVEMOOR</strong>.NU
    </div>

    <div class="contact-bar">
      <div class="contact-name">MARIEKE <span>DOORN</span></div>
      <div class="divider" style="left:407px"></div>
      <div class="contact-mail">
        <svg width="32" height="24" viewBox="0 0 32 24" fill="none" stroke="currentColor" stroke-width="2"><rect x="1" y="1" width="30" height="22" rx="2"/><path d="M1 2l15 12L31 2M1 22l11-10M31 22L20 12"/></svg>
        info@bravemoor.nu
      </div>
      <div class="divider" style="left:817px"></div>
      <div class="contact-phone">
        <svg width="30" height="36" viewBox="0 0 24 24" fill="currentColor"><path d="M6.6 10.8a15.1 15.1 0 0 0 6.6 6.6l2.2-2.2a1 1 0 0 1 1-.25 11.4 11.4 0 0 0 3.6.57 1 1 0 0 1 1 1V20a1 1 0 0 1-1 1A17 17 0 0 1 3 4a1 1 0 0 1 1-1h3.5a1 1 0 0 1 1 1c0 1.25.2 2.45.57 3.57a1 1 0 0 1-.25 1z"/></svg>
        06-12 34 56 78
      </div>
    </div>
  </div>
</div>
</body>
</html>
```